Fun relaxed Travel Photography Business Card*

Require a fun, funky and quirky but rememberable business card for a travel photographer

Industry/Entity Type

Photographer

Contact Information for Business Card

Front Card

(my name) Dane M.

Travel Photographer ( small under travel photographer) “self-proclaimed”

(website logo) wanderingsofdane.example

(Instagram logo) @wanderings_of_dane

(Instagram logo) @wanderings_of_dane_2.0 (backup for when Instagram puts Dane on timeout for bad behaviour)

Tel: N/A (removing the potential awkwardness of me not replying)

Email: (see above)

Back Card

Offending people since 1986

(Bottom right corner) “p.s. travelling made me fatTER”

Font styles to use
Serif

Colors

Designer to choose colors to be used in the design.

Requirements
Must have
• a camera
• a similar cartoon version of me as the "logo" see attached files, try to make as similar as possible

```html
<!DOCTYPE html>
<html lang="en">
<head>
<meta charset="utf-8">
<title>Dane M. — Travel Photographer Business Card</title>
<link href="https://fonts.googleapis.com/css2?family=Montserrat:wght@400;500;600&display=swap" rel="stylesheet">
<style>
  :root {
    --backdrop: #1b1b1b;
    --card: #222222;
    --card-edge: #2b2b2b;
    --gold: #f2b526;
    --ink: #f4f4f4;
    --chair-light: #f6c533;
    --chair-dark: #6b3f22;
  }
  html, body {
    margin: 0;
    width: 1200px;
    height: 900px;
    overflow: hidden;
    background: var(--backdrop);
    font-family: "Montserrat", sans-serif;
  }
  .canvas {
    position: relative;
    width: 1200px;
    height: 900px;
  }
  .card {
    position: absolute;
    left: 250px;
    width: 700px;
    height: 400px;
    background: linear-gradient(160deg, var(--card-edge), var(--card) 60%);
    box-sizing: border-box;
    overflow: hidden;
  }
  .card--back { top: 40px; }
  .card--front { top: 460px; }

  /* Back side */
  .mascot {
    position: absolute;
    left: 260px;
    top: 90px;
    width: 250px;
    height: 160px;
    border-radius: 6px;
    background: radial-gradient(ellipse at 45% 55%, var(--chair-light) 0%, #d99a1e 45%, var(--chair-dark) 100%);
  }
  .tagline {
    position: absolute;
    left: 44px;
    right: 44px;
    bottom: 44px;
    margin: 0;
    display: flex;
    align-items: baseline;
    gap: 12px;
    font-size: 14px;
    font-weight: 600;
    letter-spacing: 0.6px;
    text-transform: uppercase;
    white-space: nowrap;
  }
  .tagline__lead { color: var(--gold); }
  .tagline__rule { color: var(--ink); font-weight: 400; }
  .tagline__ps { color: var(--ink); margin-left: auto; }

  /* Front side */
  .identity {
    position: absolute;
    right: 420px;
    top: 158px;
    text-align: right;
  }
  .identity__name {
    margin: 0;
    color: var(--gold);
    font-size: 38px;
    font-weight: 600;
    letter-spacing: 3px;
    line-height: 1;
  }
  .identity__role {
    margin: 6px 0 0;
    color: var(--ink);
    font-size: 18px;
    font-weight: 400;
  }
  .divider {
    position: absolute;
    left: 302px;
    top: 145px;
    width: 2px;
    height: 110px;
    background: var(--gold);
  }
  .contacts {
    position: absolute;
    left: 328px;
    top: 148px;
    margin: 0;
    padding: 0;
    list-style: none;
    color: var(--ink);
    font-size: 16px;
    font-weight: 500;
    line-height: 26px;
  }
  .contacts__item {
    display: flex;
    align-items: center;
    gap: 10px;
    white-space: nowrap;
  }
  .contacts__icon {
    width: 12px;
    height: 12px;
    flex: none;
  }
</style>
</head>
<body>
<main class="canvas">

  <section class="card card--back" aria-label="Card back">
    <div class="mascot" role="img" aria-label="Cartoon of the photographer lounging in a yellow armchair in a floral shirt and sunglasses, with a side table holding a bottle and glass"></div>
    <p class="tagline">
      <span class="tagline__lead">Offending people since 1986</span>
      <span class="tagline__rule">|</span>
      <span class="tagline__ps">P.S. Travelling made me fatter</span>
    </p>
  </section>

  <section class="card card--front" aria-label="Card front">
    <div class="identity">
      <h1 class="identity__name">DANE M.</h1>
      <p class="identity__role">Travel Photographer</p>
    </div>
    <div class="divider"></div>
    <ul class="contacts">
      <li class="contacts__item">
        <svg class="contacts__icon" viewBox="0 0 16 16"><path d="M4 1 L6.5 4.5 L5 6.2 C6 8.4 7.6 10 9.8 11 L11.5 9.5 L15 12 L13.5 14.8 C7 14.5 1.5 9 1.2 2.5 Z" fill="var(--gold)"/></svg>
        <span>+330 2460 - 5173</span>
      </li>
      <li class="contacts__item">
        <svg class="contacts__icon" viewBox="0 0 16 16"><rect x="2" y="2" width="12" height="12" rx="2" fill="var(--gold)"/></svg>
        <span>@wanderings_of_dane</span>
      </li>
      <li class="contacts__item">
        <svg class="contacts__icon" viewBox="0 0 16 16"><rect x="1.5" y="3.5" width="13" height="9" fill="none" stroke="var(--gold)" stroke-width="1.4"/><path d="M1.5 3.5 L8 9 L14.5 3.5" fill="none" stroke="var(--gold)" stroke-width="1.4"/></svg>
        <span>info@wanderingsofdane.example</span>
      </li>
      <li class="contacts__item">
        <svg class="contacts__icon" viewBox="0 0 16 16"><g fill="none" stroke="var(--gold)" stroke-width="1.3"><circle cx="8" cy="8" r="6.5"/><ellipse cx="8" cy="8" rx="2.8" ry="6.5"/><path d="M1.5 8 H14.5 M2.5 4.8 H13.5 M2.5 11.2 H13.5"/></g></svg>
        <span>www.wanderingsofdane.example</span>
      </li>
    </ul>
  </section>

</main>
</body>
</html>
```